Gold Finch Print and Mailing Services

We are looking for a website layout design for a direct print and mailing company which prints graphics, post cards, letters, does mailing and more.

Please see attached logo, as it will be used to match color scheme of website.

Current website:
www.goldfinchprintpost.example

Websites we like:
https://velmorepress.example

Target Market(s)

Businesses / Media

Number of Pages Required

3 page

Font styles to use
Sans Serif

Requirements
Must have
• Color scheme to match logo

```html
<!DOCTYPE html>
<html lang="en">
<head>
<meta charset="utf-8">
<title>Gold Finch Print and Mailing Services</title>
<link href="https://fonts.googleapis.com/css2?family=Roboto:wght@400;500;700&family=Open+Sans:wght@400;600;700&display=swap" rel="stylesheet">
<style>
:root{
  --red:#e31e24;
  --red-soft:#e2575b;
  --dark:#2a2a2c;
  --ink:#333;
  --muted:#666;
  --light:#eeeef0;
  --white:#fff;
  --blue:#4a86b8;
  --green:#7fc47a;
  --coral:#f04c50;
  --amber:#ebab4e;
}
*{box-sizing:border-box;margin:0;padding:0}
html,body{width:1200px;height:3782px;overflow:hidden}
body{position:relative;font-family:"Open Sans",Arial,sans-serif;color:var(--ink);background:var(--white)}
.abs{position:absolute}
.header{top:0;left:0;width:1200px;height:110px;background:var(--white)}
.brand{left:100px;top:26px;display:flex;align-items:center;gap:10px;font:700 26px "Roboto",sans-serif;color:var(--red)}
.brand i{width:22px;height:22px;background:var(--red);border-radius:50%}
.phone{left:758px;top:30px;font:500 18px "Roboto",sans-serif;display:flex;align-items:center;gap:10px}
.register{left:943px;top:22px;width:123px;height:38px;background:var(--red);color:#fff;font:500 12px "Roboto",sans-serif;display:flex;align-items:center;justify-content:center}
.nav{left:400px;top:76px;display:flex;gap:22px;font:400 13px "Roboto",sans-serif;color:var(--ink)}
.nav .on{color:var(--red)}
.hero{top:110px;left:0;width:1200px;height:480px;background:linear-gradient(90deg,#eceef0,#f6f6f7)}
.hero-art{left:0;top:0;width:620px;height:480px;background:linear-gradient(135deg,#e8d14a 0%,#8fb35a 35%,#6c9c56 55%,#e57ea0 85%,#d9a3b5 100%);clip-path:polygon(0 0,100% 0,45% 100%,0 100%)}
.hero h1{left:632px;top:240px;width:520px;font:500 42px/1.25 "Roboto",sans-serif;color:#333}
.hero p{left:632px;top:350px;font:500 25px "Roboto",sans-serif;color:#333}
.btn-red{background:var(--red);color:#fff;font:700 19px "Roboto",sans-serif;display:flex;align-items:center;justify-content:center}
.dots{left:575px;top:552px;display:flex;gap:4px}
.dots i{width:10px;height:10px;border:1.5px solid #333;border-radius:50%}
.dots i:first-child{background:#333}
.section-title{width:1200px;text-align:center;font:400 35px "Roboto",sans-serif;color:#333}
.arrow{width:16px;height:26px}
.card{width:240px;background:var(--white);box-shadow:0 2px 6px rgba(0,0,0,.12)}
.card .ph{height:193px;border:1px solid #ddd}
.card .cap{height:62px;display:flex;align-items:center;justify-content:center;font:500 19px "Roboto",sans-serif;color:#2e4f7a}
.band-dark{left:0;width:1200px;background:linear-gradient(180deg,#3a3a3c,#1e1e20)}
.band-title{width:1200px;text-align:center;color:#fff;font:500 38px "Roboto",sans-serif}
.band-sub{width:1200px;text-align:center;color:#fff;font:500 30px "Roboto",sans-serif}
.btn-ghost{width:152px;height:52px;border:2px solid #fff;color:#fff;font:400 19px "Roboto",sans-serif;display:flex;align-items:center;justify-content:center}
.prod .ph{height:195px}
.prod .cap{height:55px;color:#fff;font:400 17px "Roboto",sans-serif}
.feature{width:230px;text-align:center;font:400 14px/1.65 "Open Sans",sans-serif;color:#333}
.feature .ring{width:156px;height:156px;border:2px solid var(--red);border-radius:50%;margin:0 auto 30px;display:flex;align-items:center;justify-content:center}
.catalog p{width:1200px;text-align:center;color:#fff;font:400 13px "Open Sans",sans-serif}
.quote{font:400 13px/1.7 "Open Sans",sans-serif;color:#444}
.person{font:600 22px "Open Sans",sans-serif;color:#555}
.avatar{width:90px;height:90px;border-radius:50%;background:linear-gradient(#c9c4bf,#8d8680)}
.footer{left:0;top:3450px;width:1200px;height:332px;background:linear-gradient(135deg,#f9efe6,#f3e8ee 50%,#eef1f5)}
.fcol h4{font:700 15px "Roboto",sans-serif;color:#222;margin-bottom:22px;text-transform:uppercase}
.fcol{font:400 12px/1.95 "Open Sans",sans-serif;color:#333}
.fcol li{list-style:none}
.social{display:flex;gap:14px}
.social i{width:12px;height:12px;border-radius:50%;background:var(--red)}
</style>
</head>
<body>

<header class="header abs">
  <div class="brand abs"><i></i>Gold Finch</div>
  <div class="phone abs">
    <svg width="22" height="22" viewBox="0 0 22 22"><circle cx="11" cy="11" r="10" fill="none" stroke="#e31e24" stroke-width="2"/><path d="M7 6l2 0 1 3-1.5 1a6 6 0 0 0 3.5 3.5l1-1.5 3 1v2c-5 0-9-4-9-9z" fill="#e31e24"/></svg>
    (555) 014-2290
  </div>
  <div class="register abs">&#9679;&nbsp; REGISTER / SIGN IN</div>
  <nav class="nav abs">
    <span class="on">Home</span><span>Services &amp; Print Products</span><span>Quotes &amp; Custom Orders</span><span>My Invoice Account</span><span>News</span><span>FAQ</span><span>About Us</span><span>Contact Us</span>
  </nav>
</header>

<section class="hero abs">
  <div class="hero-art abs" role="img" aria-label="Collage of printed photo cards showing citrus, a butterfly on flowers and pink roses"></div>
  <h1 class="abs">FAST AND EASY WORLD CLASS PRINTING</h1>
  <p class="abs">We're the one to help you say it.</p>
  <div class="btn-red abs" style="left:632px;top:415px;width:152px;height:52px">Read More</div>
  <div class="dots abs"><i></i><i></i><i></i><i></i></div>
</section>

<section class="abs" style="top:590px;left:0;width:1200px;height:525px;background:var(--light)">
  <h2 class="section-title abs" style="top:90px">Our Services</h2>
  <svg class="arrow abs" style="left:40px;top:283px" viewBox="0 0 16 26"><path d="M13 3L4 13l9 10" fill="none" stroke="#222" stroke-width="4"/></svg>
  <svg class="arrow abs" style="left:1150px;top:283px" viewBox="0 0 16 26"><path d="M3 3l9 10-9 10" fill="none" stroke="#222" stroke-width="4"/></svg>
  <div class="card abs" style="left:100px;top:167px"><div class="ph" role="img" aria-label="Designer working with colour swatches" style="background:linear-gradient(135deg,#d9d4cc,#8a8f99)"></div><div class="cap">GRAPHIC DESIGN</div></div>
  <div class="card abs" style="left:353px;top:167px"><div class="ph" role="img" aria-label="Colourful file folders with a magnifier" style="background:linear-gradient(135deg,#7ec04a,#f0a030 60%,#6a9bd8)"></div><div class="cap">MAIL SORTING</div></div>
  <div class="card abs" style="left:606px;top:167px"><div class="ph" role="img" aria-label="Laser printer toner cartridges" style="background:linear-gradient(135deg,#e8c400,#e0307a 50%,#1aa0d8)"></div><div class="cap">LASER PRINTING</div></div>
  <div class="card abs" style="left:859px;top:167px"><div class="ph" role="img" aria-label="Laptop with flying envelopes" style="background:linear-gradient(135deg,#f4f4f4,#c9c9c9 60%,#e8a33a)"></div><div class="cap">DIGITAL MAIL</div></div>
</section>

<section class="band-dark abs" style="top:1115px;height:410px" role="img" aria-label="Darkened backdrop of printed brochure spreads">
  <h2 class="band-title abs" style="top:108px">YOUR COMPLETE RESOURCE FOR</h2>
  <p class="band-sub abs" style="top:163px">Print &amp; Mail Service</p>
  <div class="btn-ghost abs" style="left:524px;top:240px">Read More</div>
</section>

<section class="abs" style="top:1525px;left:0;width:1200px;height:490px;background:var(--light)">
  <h2 class="section-title abs" style="top:75px">Our Products</h2>
  <svg class="arrow abs" style="left:40px;top:270px" viewBox="0 0 16 26"><path d="M13 3L4 13l9 10" fill="none" stroke="#222" stroke-width="4"/></svg>
  <svg class="arrow abs" style="left:1150px;top:270px" viewBox="0 0 16 26"><path d="M3 3l9 10-9 10" fill="none" stroke="#222" stroke-width="4"/></svg>
  <div class="card prod abs" style="left:100px;top:155px"><div class="ph" role="img" aria-label="Stack of photo post cards" style="background:linear-gradient(135deg,#f2b630,#d8452c 50%,#3a7a3a)"></div><div class="cap" style="background:var(--blue)">POST CARDS</div></div>
  <div class="card prod abs" style="left:353px;top:155px"><div class="ph" role="img" aria-label="Stack of green booklets" style="background:linear-gradient(135deg,#f2f2ee,#b7d468 60%,#8eb83e)"></div><div class="cap" style="background:var(--green)">BOOKLETS</div></div>
  <div class="card prod abs" style="left:606px;top:155px"><div class="ph" role="img" aria-label="Red envelope and letter" style="background:linear-gradient(135deg,#f4eef4,#e3d6e4 40%,#c8283c 75%)"></div><div class="cap" style="background:var(--coral)">LETTERS</div></div>
  <div class="card prod abs" style="left:859px;top:155px"><div class="ph" role="img" aria-label="Stack of white business cards" style="background:linear-gradient(135deg,#f6f6f6,#d2d2d2)"></div><div class="cap" style="background:var(--amber)">BUSINESS CARDS</div></div>
</section>

<section class="abs" style="top:2015px;left:0;width:1200px;height:380px">
  <svg class="abs" style="left:0;top:0" width="1200" height="380" viewBox="0 0 1200 380" role="img" aria-label="Red tinted backdrop of a printing press">
    <defs><linearGradient id="redBand" x1="0" y1="0" x2="0" y2="1"><stop offset="0" stop-color="#e56a6c"/><stop offset="1" stop-color="#d9383d"/></linearGradient></defs>
    <path d="M0 0H1200V355Q600 285 0 355Z" fill="url(#redBand)"/>
  </svg>
  <h2 class="band-title abs" style="top:95px">MASTERS OF VIBRANT COLOR DIGITAL</h2>
  <p class="band-sub abs" style="top:150px">Print &amp; Mailing Service</p>
  <div class="btn-ghost abs" style="left:524px;top:228px">Read More</div>
</section>

<section class="abs" style="top:2395px;left:0;width:1200px;height:390px">
  <svg class="abs" style="left:62px;top:143px" width="12" height="20" viewBox="0 0 12 20"><path d="M10 2L3 10l7 8" fill="none" stroke="#444" stroke-width="2"/></svg>
  <svg class="abs" style="left:1127px;top:143px" width="12" height="20" viewBox="0 0 12 20"><path d="M2 2l7 8-7 8" fill="none" stroke="#444" stroke-width="2"/></svg>
  <div class="feature abs" style="left:104px;top:78px"><div class="ring"><svg width="84" height="84" viewBox="0 0 84 84"><path d="M42 6a36 36 0 1 1-30 16" fill="none" stroke="#e31e24" stroke-width="5"/><path d="M6 18l7 8 8-6" fill="none" stroke="#e31e24" stroke-width="4"/><text x="42" y="52" text-anchor="middle" font-family="Roboto,sans-serif" font-weight="700" font-size="28" fill="#e31e24">24</text></svg></div>Access Your Art Files 24/7<br>with Safe Online Storage</div>
  <div class="feature abs" style="left:370px;top:78px"><div class="ring"><svg width="80" height="70" viewBox="0 0 80 70"><path d="M40 4L76 20 40 36 4 20Z" fill="#e31e24"/><path d="M4 32l36 16 36-16M4 44l36 16 36-16" fill="none" stroke="#e31e24" stroke-width="6"/></svg></div>Meet Our Ensemble of<br>Graphic Designers</div>
  <div class="feature abs" style="left:616px;top:78px"><div class="ring"><svg width="80" height="60" viewBox="0 0 80 60"><rect x="4" y="4" width="72" height="52" fill="none" stroke="#e31e24" stroke-width="5"/><path d="M4 4l36 28L76 4M4 56l26-24M76 56L50 32" fill="none" stroke="#e31e24" stroke-width="4"/></svg></div>Grab Your Best Clients with<br>Market-Focused Mail Lists!</div>
  <div class="feature abs" style="left:880px;top:78px"><div class="ring"><svg width="70" height="74" viewBox="0 0 70 74"><circle cx="35" cy="20" r="17" fill="#e31e24"/><path d="M2 74c0-22 14-34 33-34s33 12 33 34z" fill="#e31e24"/></svg></div>We are experts in the field<br>of Mail!</div>
</section>

<section class="band-dark catalog abs" style="top:2785px;height:290px" role="img" aria-label="Dark backdrop of a colour printing press">
  <h2 class="abs" style="top:78px;width:1200px;text-align:center;color:#fff;font:400 34px Roboto,sans-serif">Request Catalog</h2>
  <p class="abs" style="top:127px">Sign up for our catalog and get 20% off your next order. Pretty sweet, we know.</p>
  <div class="abs" style="left:410px;top:178px;width:286px;height:40px;background:#222;border:1px solid #555;color:#ddd;font:400 13px 'Open Sans',sans-serif;padding:10px 20px">Enter your Email</div>
  <div class="btn-red abs" style="left:696px;top:178px;width:102px;height:40px;font-size:14px;font-weight:500">REQUEST</div>
</section>

<section class="abs" style="top:3075px;left:0;width:1200px;height:375px">
  <h2 class="section-title abs" style="top:78px">Testimonial</h2>
  <div class="abs" style="top:118px;width:1200px;text-align:center;color:var(--red);font:700 30px Georgia,serif">&#8220;</div>
  <p class="quote abs" style="left:95px;top:200px;width:360px;text-align:right">&#8220; Lorem ipsum dolor sit amet, consectetur adipisicing elit, sed do eiusmod tempor incididunt ut labore et dolore.</p>
  <div class="person abs" style="left:255px;top:250px;width:200px;text-align:right">Marcus Hale</div>
  <div class="avatar abs" style="left:495px;top:195px" role="img" aria-label="Portrait of client Marcus Hale"></div>
  <div class="avatar abs" style="left:615px;top:195px;background:linear-gradient(#e3dcd6,#7a6a60)" role="img" aria-label="Portrait of client Irene Voss"></div>
  <p class="quote abs" style="left:745px;top:193px;width:360px">&#8220; Lorem ipsum dolor sit amet, consectetur adipisicing elit, sed do eiusmod tempor incididunt ut labore et dolore.</p>
  <div class="person abs" style="left:745px;top:245px">Irene Voss</div>
</section>

<footer class="footer abs">
  <div class="fcol abs" style="left:97px;top:67px;width:225px"><h4>About Us</h4><p style="text-align:justify">Even in today's digital marketplace, mail continues to be one of the most effective forms of communication.</p></div>
  <ul class="fcol abs" style="left:377px;top:60px"><h4>Quick Links</h4><li>&rsaquo; About Us</li><li>&rsaquo; FAQ</li><li>&rsaquo; Get A Quote</li><li>&rsaquo; Recent Work</li><li>&rsaquo; Latest News</li><li>&rsaquo; Brochure</li></ul>
  <ul class="fcol abs" style="left:560px;top:60px"><h4>Information</h4><li>Home</li><li>Invoice</li><li>Order History</li><li>Terms &amp; Conditions</li></ul>
  <ul class="fcol abs" style="left:758px;top:60px;width:170px"><h4>Contact</h4>
    <li style="color:#333"><span style="color:var(--red)">&#9679;</span>&nbsp; Gold Finch Print Post,</li>
    <li style="padding-left:22px">Lorem Ipsum is Simple,</li>
    <li style="padding-left:22px">Lorem Ipsum.</li>
    <li><span style="color:var(--red)">&#9742;</span>&nbsp; (555) 014-2290</li>
    <li><span style="color:var(--red)">&#9993;</span>&nbsp; hello@goldfinch.example</li>
  </ul>
  <div class="fcol abs" style="left:980px;top:60px"><h4>Follow Us On</h4><div class="social"><i></i><i></i><i></i><i></i></div></div>
  <svg class="abs" style="left:1143px;top:210px" width="28" height="28" viewBox="0 0 28 28"><circle cx="14" cy="14" r="13" fill="#777"/><path d="M8 17l6-6 6 6" fill="none" stroke="#fff" stroke-width="3"/></svg>
  <div class="abs" style="left:97px;top:283px;width:1006px;height:1px;background:#ccc"></div>
  <p class="abs" style="top:300px;width:1200px;text-align:center;font:400 11px 'Open Sans',sans-serif;color:#444">Copyright &copy; 2018. All Rights Reserved.</p>
</footer>

</body>
</html>
```